Brellwick Finance Stationary Design

We have selected a logo as our winner, we now need a full stationary set to be in the same theme.
Required:
- Letter Head
- Business Card Template
- Custom Envelopes
- A5 Notepad Design (Front cover and content pages. Content pages blank(no lines) but with our branding on them,)
- With Compliments Slip
Updates

Hey All,

We have changed the colour scheme of our logo. Our apologies if anyone has begun designing based off the old scheme. Please see the updated scheme in the brief,

Tobin

Target Market(s)

Target market is experienced property developers and financial institutions.

Industry/Entity Type

Commercial Finance

Font styles to use
Serif

Colors
0054AA
0677BA
7BADD7
CADEEF
E8F1F8
0094D4
00A9DD
6FCCEA
C7EBF8
E9F6FB
00AB8E
00BBA5
67D7C9
C6EFE9
E9F9F6
59FF00
82FF00
B8FF75
E3FFCB
F4FFEA

```html
<!DOCTYPE html>
<html lang="en">
<head>
<meta charset="utf-8">
<title>Brellwick Finance Stationery Set</title>
<link href="https://fonts.googleapis.com/css2?family=Tinos:wght@400;700&display=swap" rel="stylesheet">
<style>
  :root {
    --brand-blue: #0054AA;
    --brand-teal: #00AB8E;
    --ink: #111111;
    --rule-grey: #c4c4c8;
    --paper: #ffffff;
    --backdrop: #ecebe7;
    --font-text: "Tinos", "Times New Roman", serif;
  }
  * { box-sizing: border-box; margin: 0; padding: 0; }
  html, body { width: 1200px; height: 996px; overflow: hidden; }
  body { background: var(--backdrop); font-family: var(--font-text); color: var(--ink); position: relative; }

  .sheet { position: absolute; background: var(--paper); box-shadow: 0 2px 6px rgba(0,0,0,.18); overflow: hidden; }
  .bar { position: absolute; }
  .bar--teal { background: var(--brand-teal); }
  .bar--blue { background: var(--brand-blue); }

  /* small corner marks */
  .mark-tl, .mark-br { position: absolute; width: 24px; height: 28px; }
  .mark-tl { left: 0; top: 0; }
  .mark-tl .bar--teal { left: 0; top: 0; width: 12px; height: 28px; }
  .mark-tl .bar--blue { left: 12px; top: 0; width: 12px; height: 17px; }
  .mark-br { right: 0; bottom: 0; }
  .mark-br .bar--blue { left: 0; bottom: 0; width: 12px; height: 17px; }
  .mark-br .bar--teal { right: 0; bottom: 0; width: 12px; height: 28px; }

  /* brand name lockup */
  .brand { position: absolute; display: flex; align-items: center; gap: 6px; font-weight: 700; color: var(--brand-blue); white-space: nowrap; letter-spacing: .3px; }
  .brand__square { display: block; background: var(--brand-teal); }

  /* contact block */
  .contact { position: absolute; }
  .contact__name { font-size: 11px; }
  .contact__role { font-size: 6px; font-weight: 700; margin-bottom: 3px; }
  .contact__line { display: flex; align-items: center; gap: 4px; font-size: 6px; font-weight: 700; line-height: 9px; }
  .contact__line svg { width: 6px; height: 6px; fill: var(--ink); }
  .contact__row { display: flex; gap: 8px; }

  /* letterhead */
  .letterhead { left: 33px; top: 50px; width: 633px; height: 895px; }
  .letterhead__rule { position: absolute; left: 93px; right: 0; top: 87px; height: 4px; background: var(--rule-grey); }

  .card { width: 269px; height: 153px; top: 211px; }
  .card--front { left: 62px; }
  .card--back { left: 368px; }
  .card__name { color: var(--brand-teal); }
  .card__name span { color: var(--brand-blue); }

  .envelope { left: 60px; top: 488px; width: 591px; height: 289px; }

  .notepad { left: 692px; top: 66px; width: 443px; height: 634px; }
  .notepad__rule { position: absolute; left: 0; right: 0; top: 34px; height: 3px; background: var(--rule-grey); }

  .slip { left: 693px; top: 744px; width: 320px; height: 153px; }
  .slip__title { position: absolute; left: 24px; top: 19px; font-size: 18px; }
  .slip__from { position: absolute; left: 24px; top: 86px; font-size: 9px; }
</style>
</head>
<body>

<svg width="0" height="0" style="position:absolute">
  <defs>
    <symbol id="icon-phone" viewBox="0 0 10 10"><path d="M2 0.5l2 2-1 1.2a6 6 0 0 0 3.3 3.3l1.2-1 2 2-1.3 1.5C4.5 9.3.7 5.5.5 1.8z"/></symbol>
    <symbol id="icon-mail" viewBox="0 0 10 10"><path d="M0 2h10v6H0zM1 3l4 3 4-3v-.2H1z" fill-rule="evenodd"/></symbol>
    <symbol id="icon-pin" viewBox="0 0 10 10"><path d="M5 0a3.5 3.5 0 0 1 3.5 3.5C8.5 6 5 10 5 10S1.5 6 1.5 3.5A3.5 3.5 0 0 1 5 0zm0 2a1.5 1.5 0 1 0 0 3 1.5 1.5 0 0 0 0-3z" fill-rule="evenodd"/></symbol>
  </defs>
</svg>

<!-- Letterhead -->
<section class="sheet letterhead" aria-label="Letterhead">
  <div class="bar bar--teal" style="left:0;top:0;width:38px;height:132px"></div>
  <div class="bar bar--blue" style="left:38px;top:0;width:38px;height:100px"></div>
  <div class="brand" style="left:90px;top:28px;font-size:20px">
    <span class="brand__square" style="width:12px;height:12px"></span>Brellwick Finance
  </div>
  <div class="letterhead__rule"></div>
  <div class="contact" style="left:392px;top:16px">
    <p class="contact__name">First Last name</p>
    <p class="contact__role">Founder</p>
    <p class="contact__line"><svg><use href="#icon-phone"/></svg>+1 123-456-7890</p>
    <p class="contact__line"><svg><use href="#icon-mail"/></svg>www.brellwick.com</p>
    <p class="contact__line"><svg><use href="#icon-pin"/></svg>your office address will goes here</p>
  </div>
  <div class="bar bar--blue" style="right:38px;bottom:0;width:38px;height:99px"></div>
  <div class="bar bar--teal" style="right:0;bottom:0;width:38px;height:131px"></div>
</section>

<!-- Business card front -->
<section class="sheet card card--front" aria-label="Business card front">
  <div class="mark-tl"><div class="bar bar--teal"></div><div class="bar bar--blue"></div></div>
  <div class="brand" style="left:50%;top:62px;transform:translateX(-50%);font-size:20px">
    <span class="brand__square" style="width:12px;height:12px"></span>Brellwick Finance
  </div>
  <div class="mark-br"><div class="bar bar--blue"></div><div class="bar bar--teal"></div></div>
</section>

<!-- Business card back -->
<section class="sheet card card--back" aria-label="Business card back">
  <div class="mark-tl"><div class="bar bar--teal"></div><div class="bar bar--blue"></div></div>
  <div class="brand" style="right:16px;top:22px;font-size:12px;gap:4px">
    <span class="brand__square" style="width:7px;height:7px"></span>Brellwick Finance
  </div>
  <div class="contact" style="left:91px;top:70px">
    <p class="contact__name card__name">First <span>Last name</span></p>
    <p class="contact__role">Founder</p>
  </div>
  <div class="contact" style="left:22px;top:122px">
    <p class="contact__line"><svg><use href="#icon-phone"/></svg>+1 123-456-7890</p>
    <div class="contact__row">
      <p class="contact__line"><svg><use href="#icon-mail"/></svg>www.brellwick.com</p>
      <p class="contact__line"><svg><use href="#icon-pin"/></svg>your office address will goes here</p>
    </div>
  </div>
  <div class="mark-br"><div class="bar bar--blue"></div><div class="bar bar--teal"></div></div>
</section>

<!-- Envelope -->
<section class="sheet envelope" aria-label="Envelope">
  <div class="mark-tl"><div class="bar bar--teal" style="height:36px"></div><div class="bar bar--blue" style="height:25px"></div></div>
  <div class="brand" style="left:33px;top:32px;font-size:18px">
    <span class="brand__square" style="width:11px;height:11px"></span>Brellwick Finance
  </div>
  <div class="contact" style="left:30px;top:192px">
    <p class="contact__name">First Last name</p>
    <p class="contact__role">Founder</p>
    <p class="contact__line"><svg><use href="#icon-phone"/></svg>+1 123-456-7890</p>
    <p class="contact__line"><svg><use href="#icon-mail"/></svg>www.brellwick.com</p>
    <p class="contact__line"><svg><use href="#icon-pin"/></svg>your office address will goes here</p>
  </div>
  <div class="mark-br" style="height:37px"><div class="bar bar--blue" style="height:25px"></div><div class="bar bar--teal" style="height:37px"></div></div>
</section>

<!-- Notepad cover -->
<section class="sheet notepad" aria-label="A5 notepad cover">
  <div class="notepad__rule"></div>
  <div class="mark-tl" style="top:37px"><div class="bar bar--teal"></div><div class="bar bar--blue"></div></div>
  <div class="brand" style="left:50%;top:294px;transform:translateX(-50%);font-size:28px;gap:8px">
    <span class="brand__square" style="width:16px;height:16px"></span>Brellwick Finance
  </div>
  <div class="mark-br"><div class="bar bar--blue"></div><div class="bar bar--teal"></div></div>
</section>

<!-- With compliments slip -->
<section class="sheet slip" aria-label="With compliments slip">
  <div class="mark-tl"><div class="bar bar--teal"></div><div class="bar bar--blue"></div></div>
  <p class="slip__title">With Compliments</p>
  <p class="slip__from">From : -</p>
  <div class="brand" style="left:24px;top:110px;font-size:14px;gap:5px">
    <span class="brand__square" style="width:8px;height:8px"></span>Brellwick Finance
  </div>
  <div class="mark-br"><div class="bar bar--blue"></div><div class="bar bar--teal"></div></div>
</section>

</body>
</html>
```